Orvel Prime - Letter Head

My company is a residential and commercial cleaning company , which is located in Abu Dhabi, UAE.
I am looking for a creative letterhead reflects the professional and reflects professionalism and send the feeling of relax and comfort.
The color which will be used it has to be selected carefully in prospective of colors psychological effects, so every color to be used should be for a reason.
Also, reflecting my company colors in an attractive way.
Regarding the information which it should contains, it has to show the address, contacts , telephones an, email address and website.
Also, my company logo is attached
Residential

```html
<!DOCTYPE html>
<html lang="en">
<head>
<meta charset="UTF-8">
<title>Orvel Prime – Letterhead</title>
<link href="https://fonts.googleapis.com/css2?family=Questrial&display=swap" rel="stylesheet">
<style>
  :root {
    --paper: #ffffff;
    --brand-blue: #1c4f8c;
    --brand-green: #5fae2e;
    --leaf-light: #b9e06a;
    --leaf-mid: #7cc242;
    --leaf-deep: #3f8f25;
  }
  html, body {
    margin: 0;
    padding: 0;
    overflow: hidden;
    background: var(--paper);
  }
  .letterhead {
    position: relative;
    width: 851px;
    height: 1200px;
    background: var(--paper);
    overflow: hidden;
    font-family: "Questrial", "Century Gothic", sans-serif;
  }
  .brand {
    position: absolute;
    top: 78px;
    right: 120px;
    display: flex;
    align-items: center;
    gap: 18px;
  }
  .brand-name {
    font-size: 58px;
    line-height: 1;
    color: var(--brand-blue);
    letter-spacing: -0.5px;
  }
  .brand-dot {
    width: 70px;
    height: 70px;
    border-radius: 50%;
    background: var(--brand-green);
  }
  .plant-art {
    position: absolute;
    left: 0;
    bottom: 0;
    width: 400px;
    height: 345px;
    border-top-right-radius: 70% 80%;
    background: radial-gradient(ellipse at 35% 60%, var(--leaf-light) 0%, var(--leaf-mid) 45%, var(--leaf-deep) 100%);
    opacity: 0.9;
  }
  .contact {
    position: absolute;
    left: 411px;
    top: 1028px;
    color: var(--brand-blue);
  }
  .contact-address {
    margin: 0;
    font-size: 14px;
    line-height: 17px;
    width: 380px;
    font-weight: 400;
  }
  .contact-lines {
    margin: 12px 0 0;
    font-size: 19px;
    font-weight: 400;
  }
  .contact-lines .divider {
    color: var(--brand-green);
    margin: 0 10px;
  }
  .contact-web {
    margin: 12px 0 0;
    font-size: 31px;
    color: var(--brand-green);
    letter-spacing: 0.5px;
  }
</style>
</head>
<body>
  <main class="letterhead">
    <header class="brand">
      <span class="brand-name">Orvel Prime</span>
      <span class="brand-dot"></span>
    </header>

    <div class="plant-art" role="img" aria-label="Illustration of a fresh green leafy sprout with dew drops"></div>

    <footer class="contact">
      <p class="contact-address">Address Line 1, Address Line 2, Address Line 3,<br>Address Line 4, Address Line 5</p>
      <p class="contact-lines">Telephone No.<span class="divider">|</span>info@orvelprime.com</p>
      <p class="contact-web">www.orvelprime.com</p>
    </footer>
  </main>
</body>
</html>
```